We are a family owned wine company in Australia just starting out and we are looking for a label design. We live along Kestrel Rise, the sheoak is a tree native to South Eastern Australia. We are looking for something bright, colourful and unique. The only thing unique to the sheoak tree is that the endangered Glossy Black Cockatoo feeds entirely on this tree.

The business name is Kestrel Rise Wines, but it doesn't have to say 'Wines' on the front label - we will put it in small writing on the back label. There is no business logo yet.

The wine is mid to high range in price and quality.

Our first wine we are bottling is a 2021 Sparkling Shiraz.

Attached is the bottle and label dimensions.

```html
<!DOCTYPE html>
<html lang="en">
<head>
<meta charset="utf-8">
<title>Kestrel Rise – 2021 Sparkling Shiraz Label</title>
<link rel="stylesheet" href="https://fonts.googleapis.com/css2?family=Oswald:wght@300;400&display=swap">
<style>
  :root {
    --page-bg: #f2f2f2;
    --label-black: #050505;
    --title-mint: #eaf6e4;
    --accent-pink: #e0197d;
    --band-text: #f6e6ef;
    --splash-orange: #f39a1c;
    --splash-pink: #e8459a;
    --splash-peach: #f3a977;
    --splash-lilac: #d9a0d6;
  }
  * { margin: 0; padding: 0; box-sizing: border-box; }
  html, body {
    width: 1200px;
    height: 1049px;
    overflow: hidden;
    background: var(--page-bg);
  }
  .canvas {
    position: relative;
    width: 1200px;
    height: 1049px;
  }
  .wine-label {
    position: absolute;
    left: 270px;
    top: 72px;
    width: 660px;
    height: 904px;
    background: var(--label-black);
    overflow: hidden;
    font-family: "Oswald", "Arial Narrow", sans-serif;
  }
  .label-artwork {
    position: absolute;
    left: 0;
    top: 10px;
    width: 660px;
    height: 640px;
  }
  .brand-name {
    position: absolute;
    left: 53px;
    top: 660px;
    font-weight: 300;
    font-size: 82px;
    line-height: 1;
    letter-spacing: 0.5px;
    color: var(--title-mint);
    white-space: nowrap;
  }
  .vintage-band {
    position: absolute;
    left: 17px;
    top: 768px;
    width: 445px;
    height: 30px;
    background: linear-gradient(90deg, rgba(224,25,125,0) 0%, var(--accent-pink) 18%, var(--accent-pink) 100%);
    display: flex;
    align-items: center;
    justify-content: flex-end;
    padding-right: 10px;
  }
  .vintage-band span {
    font-weight: 400;
    font-size: 22px;
    line-height: 1;
    letter-spacing: 1px;
    color: var(--band-text);
    white-space: nowrap;
  }
  .volume {
    position: absolute;
    right: 198px;
    top: 816px;
    font-weight: 300;
    font-size: 28px;
    line-height: 1;
    color: var(--accent-pink);
  }
</style>
</head>
<body>
  <main class="canvas">
    <section class="wine-label">
      <svg class="label-artwork" viewBox="0 0 660 640" role="img"
           aria-label="Illustration: glossy black cockatoo perched on a tree branch in front of bright pink, orange, lilac and green paint splashes">
        <defs>
          <radialGradient id="splash-glow" cx="50%" cy="45%" r="55%">
            <stop offset="0%" stop-color="var(--splash-orange)"/>
            <stop offset="35%" stop-color="var(--splash-peach)"/>
            <stop offset="65%" stop-color="var(--splash-pink)"/>
            <stop offset="85%" stop-color="var(--splash-lilac)" stop-opacity="0.7"/>
            <stop offset="100%" stop-color="var(--label-black)" stop-opacity="0"/>
          </radialGradient>
          <linearGradient id="bird-shade" x1="0" y1="0" x2="0" y2="1">
            <stop offset="0%" stop-color="#2a2f3a"/>
            <stop offset="100%" stop-color="#1a1d24"/>
          </linearGradient>
        </defs>
        <ellipse cx="330" cy="290" rx="330" ry="290" fill="url(#splash-glow)"/>
        <ellipse cx="420" cy="380" rx="130" ry="240" fill="url(#bird-shade)" opacity="0.85"/>
      </svg>

      <h1 class="brand-name">KESTREL RISE</h1>
      <div class="vintage-band"><span>2021 SPARKLING SHIRAZ</span></div>
      <p class="volume">700 ml</p>
    </section>
  </main>
</body>
</html>
```